to-go container produts catalogue

we sell different kinds of to-go containers and need to make a catalogue for our cosumers.
Most of them are restraunts owner and some of them are distrunutors.
Our company named "Bright Meadow Packaging"
Our website is www.brightmeadowpackaging.com
our produts are quite like we showed on web.
We also have other produtcs need to be showed in the catalogue
We have different product lines and each type have different size.
We hope the catalogue is simple and clear. maybe a little industrial style

```html
<!DOCTYPE html>
<html lang="en">
<head>
<meta charset="utf-8">
<title>Bright Meadow Packaging — Product Catalogue</title>
<link rel="stylesheet" href="https://fonts.googleapis.com/css2?family=Montserrat:wght@500;600;700;800&family=Open+Sans:wght@400;600;700&display=swap">
<style>
:root{
  --bg:#e5e7e6;
  --page:#ffffff;
  --band:#9fd5ae;
  --band-dark:#86c99a;
  --mint-soft:#d5ede0;
  --mint-pale:#e8f5ec;
  --line:#86c69a;
  --ink:#37443c;
  --ink-soft:#5a6a60;
  --green-deep:#2f8a52;
  --navy:#1f3f78;
}
*{box-sizing:border-box;margin:0;padding:0}
html,body{width:1200px;height:4559px;overflow:hidden}
body{background:var(--bg);font-family:"Open Sans",Arial,sans-serif;color:var(--ink);position:relative}

.spread{position:absolute;left:72px;width:1072px;height:537px;display:flex;gap:18px}
.page{width:527px;height:537px;background:var(--page);padding:16px;display:flex;flex-direction:column;position:relative}

/* section band */
.band{height:34px;margin-bottom:16px;background:linear-gradient(90deg,var(--band-dark),var(--band));
  clip-path:polygon(0 0,100% 0,calc(100% - 20px) 100%,0 100%);
  font-family:"Montserrat",sans-serif;font-weight:700;font-size:16px;color:#fff;line-height:34px;padding-left:66px;letter-spacing:.2px}
.page.right .band{clip-path:polygon(0 0,100% 0,100% 100%,20px 100%);text-align:right;padding:0 30px 0 0;
  background:linear-gradient(90deg,var(--band),var(--band-dark))}

.grid{flex:1;display:grid;grid-template-columns:1fr 1fr;grid-template-rows:1fr 1fr;gap:14px 16px}
.stack{flex:1;display:grid;grid-template-rows:1fr 1fr;gap:14px}
.pair{display:grid;grid-template-columns:1fr 1fr;gap:16px}

.card{border:2px solid var(--line);border-radius:8px;overflow:hidden;display:flex;flex-direction:column;background:#fff}
.card-title{background:var(--mint-soft);min-height:32px;padding:4px 10px;display:flex;align-items:center;justify-content:center;text-align:center;
  font-size:10.5px;line-height:1.2;color:var(--ink)}
.shot{flex:1;position:relative}
.ph{position:absolute;left:50%;top:10px;transform:translateX(-50%);width:128px;height:80px;border-radius:12px}
.ph.tall{width:72px;height:96px;border-radius:6px 6px 14px 14px}
.ph.round{width:124px;height:76px;border-radius:50% 50% 40% 40%/30% 30% 70% 70%}
.ph.cup{width:96px;height:72px;border-radius:40% 40% 30% 30%}
.ph.glass{width:64px;height:100px;border-radius:4px 4px 16px 16px}
.ph.long{width:150px;height:34px;top:34px;border-radius:4px}
.ph.white{background:linear-gradient(160deg,#ffffff,#d8dcda)}
.ph.black{background:linear-gradient(160deg,#7a7e80,#1c1e20)}
.ph.kraft{background:linear-gradient(160deg,#deb274,#a97636)}
.ph.boxblack{background:linear-gradient(160deg,#555,#141414)}
.ph.clear{background:linear-gradient(160deg,#f6f8f8,#d9e0e1)}
.ph.silver{background:linear-gradient(160deg,#f0f1f2,#a3a7ab)}
.ph.wood{background:linear-gradient(90deg,#f3f1ec 0 55%,#d9b98a 55%)}
.code{position:absolute;right:12px;bottom:4px;font-size:11px;color:var(--ink)}

.meta{background:var(--mint-pale);padding:5px 8px;display:flex;justify-content:space-between;align-items:flex-end;min-height:50px}
.specs{font-size:7px;line-height:1.3;color:var(--ink)}
.icons{display:flex;gap:4px}
.icon{width:27px;text-align:center;font-size:4.4px;font-weight:700;line-height:1.1;color:var(--ink);display:flex;flex-direction:column;align-items:center}
.icon svg{width:13px;height:13px;margin-bottom:2px;color:var(--ink)}

/* wide cards */
.wide .card-title{justify-content:center;position:relative}
.wide .card-title .num{position:absolute;left:12px;font-size:10.5px}
.variants{flex:1;display:flex;justify-content:space-around;align-items:flex-end;padding:8px 14px 6px}
.variant{display:flex;flex-direction:column;align-items:center;gap:6px;font-size:9.5px;color:var(--ink)}
.variant .art{width:90px;height:78px;border-radius:8px}
.art.bag{background:linear-gradient(160deg,#ffffff,#dfe3e1);border:1px solid #b9c2bd}
.art.trash{background:linear-gradient(160deg,#fafafa,#e3e5e4);border:1px solid #b9c2bd;width:80px;height:70px;border-radius:40% 40% 12px 12px}
.art.paperbag{background:linear-gradient(160deg,#ffffff,#e4e6e5);border:1px solid #b9c2bd}
.card.empty{background:#fff}

/* cover */
.cover .pattern{position:absolute;inset:16px;background:linear-gradient(135deg,#bfe6cc,#86c89c 45%,#d9efe0);border-radius:2px}
.intro{position:absolute;left:149px;top:147px;width:235px;height:232px;background:#fff;padding:14px 14px;text-align:center;font-size:8.6px;line-height:1.4;color:var(--ink)}
.intro p{margin-bottom:8px}
.intro .line{display:flex;flex-direction:column;align-items:center;margin-top:6px;font-size:8.4px}
.intro svg{width:10px;height:10px;margin-bottom:2px;color:var(--ink)}
.brand-box{position:absolute;left:172px;top:412px;width:182px;height:96px;background:#fff;display:flex;align-items:center;justify-content:center;text-align:center;
  font-family:"Montserrat",sans-serif;font-weight:800;font-size:21px;line-height:1.1;color:var(--navy)}

/* custom printing */
.lead{background:var(--mint-pale);color:var(--green-deep);font-size:12px;padding:3px 8px;margin:-4px 0 12px;width:440px}
.promo{width:270px;font-size:12px;line-height:1.3;color:var(--ink-soft)}
.promo p{margin-bottom:11px}
.promo b{display:block;color:var(--green-deep);font-weight:600}
.promo .cta{color:var(--green-deep);font-weight:700;font-size:13px}
.collage{position:absolute;left:228px;top:127px;width:285px;height:396px;
  background:linear-gradient(160deg,#d9c7a8,#9a7a52 60%,#4f5b52);clip-path:polygon(100% 0,100% 100%,0 100%)}

/* news */
.news{flex:1;border:2px solid var(--mint-soft);position:relative}
.headline{position:absolute;left:10px;top:8px;width:130px;background:var(--mint-soft);color:var(--green-deep);font-weight:700;font-size:10px;padding:2px 4px}
.col{position:absolute;font-size:7.4px;line-height:1.25;color:var(--ink-soft);text-align:justify}
.col.a{left:10px;top:28px;width:130px;height:440px;overflow:hidden}
.col.b{left:260px;top:8px;width:236px}
.news-photo{position:absolute;left:146px;top:185px;width:220px;height:168px;border-radius:8px;background:linear-gradient(160deg,#2e2e2e,#6d4a2c 55%,#e6e6e6)}
</style>
</head>
<body>

<svg width="0" height="0" style="position:absolute" aria-hidden="true">
  <symbol id="i-recycle" viewBox="0 0 24 24"><path d="M12 3l8 14H4z" fill="none" stroke="currentColor" stroke-width="2" stroke-linejoin="round"/><path d="M9 13h6" stroke="currentColor" stroke-width="2"/></symbol>
  <symbol id="i-micro" viewBox="0 0 24 24"><rect x="2" y="5" width="20" height="14" rx="2" fill="none" stroke="currentColor" stroke-width="2"/><rect x="5" y="8" width="10" height="8" fill="currentColor"/><circle cx="18.5" cy="12" r="1.5" fill="currentColor"/></symbol>
  <symbol id="i-leak" viewBox="0 0 24 24"><circle cx="12" cy="12" r="10" fill="none" stroke="currentColor" stroke-width="2"/><path d="M12 6c3 4 4 6 4 8a4 4 0 0 1-8 0c0-2 1-4 4-8z" fill="currentColor"/><path d="M5 5l14 14" stroke="currentColor" stroke-width="2"/></symbol>
  <symbol id="i-pin" viewBox="0 0 24 24"><path d="M12 2a7 7 0 0 0-7 7c0 5 7 13 7 13s7-8 7-13a7 7 0 0 0-7-7zm0 9.5a2.5 2.5 0 1 1 0-5 2.5 2.5 0 0 1 0 5z" fill="currentColor"/></symbol>
  <symbol id="i-phone" viewBox="0 0 24 24"><path d="M6.6 10.8a15 15 0 0 0 6.6 6.6l2.2-2.2a1 1 0 0 1 1-.25 11 11 0 0 0 3.6.6 1 1 0 0 1 1 1V20a1 1 0 0 1-1 1A17 17 0 0 1 3 4a1 1 0 0 1 1-1h3.5a1 1 0 0 1 1 1 11 11 0 0 0 .6 3.6 1 1 0 0 1-.25 1z" fill="currentColor"/></symbol>
  <symbol id="i-mail" viewBox="0 0 24 24"><rect x="2" y="5" width="20" height="14" rx="1" fill="currentColor"/><path d="M2 6l10 7 10-7" fill="none" stroke="#fff" stroke-width="1.6"/></symbol>
</svg>

<!-- Cover -->
<section class="spread cover" style="top:62px">
  <div class="page">
    <div class="pattern" role="img" aria-label="Mosaic of disposable food containers, cups and cutlery in soft green tones"></div>
    <div class="intro">
      <p>We at Bright Meadow Packaging are committed to providing high quality disposable goods to our customers. We are a small business based in Los Angeles, California. We specialize in customization of cutlery, napkins, and other disposables.</p>
      <p>Contact us 24/7 our team of sales is ready to serve.</p>
      <div class="line"><svg><use href="#i-pin"/></svg>1250 Orchard Ave.<br>Fairview, CA 90000</div>
      <div class="line"><svg><use href="#i-phone"/></svg>555-014-2288</div>
      <div class="line"><svg><use href="#i-mail"/></svg>cs@brightmeadowpackaging.com</div>
    </div>
  </div>
  <div class="page">
    <div class="pattern" role="img" aria-label="Mosaic of take-out boxes, bowls and cups in mint green tones"></div>
    <div class="brand-box">Bright Meadow<br>Packaging</div>
  </div>
</section>

<!-- Clamshell -->
<section class="spread" style="top:620px">
  <div class="page">
    <div class="band">Clamshell MFPP Container</div>
    <div class="grid">
      <div class="card"><div class="card-title">5.25" x 5.25", Clamshell MFPP Container,<br>Center Slide</div><div class="shot"><div class="ph white" role="img" aria-label="White square clamshell container"></div><span class="code"># C1</span></div><div class="meta"><div class="specs">Capacity: 15 OZ<br>Color: White<br>Material: MFPP<br>Quantity: 250 PC<br>Case Weight: 17.64 LB</div><div class="icons"><span class="icon"><svg><use href="#i-recycle"/></svg>RECYCLABLE</span><span class="icon"><svg><use href="#i-micro"/></svg>MICROWAVE SAFE</span></div></div></div>
      <div class="card"><div class="card-title">6" x 6", Clamshell MFPP Container,<br>Corner Lock</div><div class="shot"><div class="ph white" role="img" aria-label="White open clamshell container"></div><span class="code"># C2</span></div><div class="meta"><div class="specs">Capacity: 16 OZ<br>Color: White<br>Material: MFPP<br>Quantity: 250 PC<br>Case Weight: 15.43 LB</div><div class="icons"><span class="icon"><svg><use href="#i-recycle"/></svg>RECYCLABLE</span><span class="icon"><svg><use href="#i-micro"/></svg>MICROWAVE SAFE</span></div></div></div>
      <div class="card"><div class="card-title">9" x 6" Tall, Clamshell MFPP Container,<br>Corner Lock</div><div class="shot"><div class="ph white" role="img" aria-label="White tall clamshell container"></div><span class="code"># C3</span></div><div class="meta"><div class="specs">Color: White<br>Material: MFPP<br>Quantity: 120 PC<br>Case Weight: 11.24 LB</div><div class="icons"><span class="icon"><svg><use href="#i-recycle"/></svg>RECYCLABLE</span><span class="icon"><svg><use href="#i-micro"/></svg>MICROWAVE SAFE</span></div></div></div>
      <div class="card"><div class="card-title">9" x 6" Tall, Clamshell MFPP Container,<br>Corner Lock</div><div class="shot"><div class="ph white" role="img" aria-label="White tall clamshell container"></div><span class="code"># C4</span></div><div class="meta"><div class="specs">Color: White<br>Material: MFPP<br>Quantity: 120 PC<br>Case Weight: 11.24 LB</div><div class="icons"><span class="icon"><svg><use href="#i-recycle"/></svg>RECYCLABLE</span><span class="icon"><svg><use href="#i-micro"/></svg>MICROWAVE SAFE</span></div></div></div>
    </div>
  </div>
  <div class="page right">
    <div class="band">Clamshell MFPP Container</div>
    <div class="grid">
      <div class="card"><div class="card-title">8" x 8", Clamshell MFPP Container,<br>Center Slide</div><div class="shot"><div class="ph white" role="img" aria-label="White square clamshell container"></div><span class="code"># C5</span></div><div class="meta"><div class="specs">Color: White<br>Material: MFPP<br>Quantity: 120 PC<br>Case Weight: 14.51 LB</div><div class="icons"><span class="icon"><svg><use href="#i-recycle"/></svg>RECYCLABLE</span><span class="icon"><svg><use href="#i-micro"/></svg>MICROWAVE SAFE</span></div></div></div>
      <div class="card"><div class="card-title">8" x 8", Clamshell MFPP 3-Compartment<br>Container, Corner Lock</div><div class="shot"><div class="ph white" role="img" aria-label="White three-compartment clamshell"></div><span class="code"># C6</span></div><div class="meta"><div class="specs">Color: White<br>Material: MFPP<br>Quantity: 120 PC<br>Case Weight: 14.55 LB</div><div class="icons"><span class="icon"><svg><use href="#i-recycle"/></svg>RECYCLABLE</span><span class="icon"><svg><use href="#i-micro"/></svg>MICROWAVE SAFE</span></div></div></div>
      <div class="card"><div class="card-title">9" x 9" , Clamshell MFPP Container,<br>Corner Lock</div><div class="shot"><div class="ph white" role="img" aria-label="White open clamshell container"></div><span class="code"># C7</span></div><div class="meta"><div class="specs">Color: White<br>Material: MFPP<br>Quantity: 120 PC<br>Case Weight: 17.42 LB</div><div class="icons"><span class="icon"><svg><use href="#i-recycle"/></svg>RECYCLABLE</span><span class="icon"><svg><use href="#i-micro"/></svg>MICROWAVE SAFE</span></div></div></div>
      <div class="card"><div class="card-title">9" x 9", Clamshell MFPP 3-Compartment<br>Container, Corner Lock</div><div class="shot"><div class="ph white" role="img" aria-label="White three-compartment clamshell"></div><span class="code"># C8</span></div><div class="meta"><div class="specs">Color: White<br>Material: MFPP<br>Quantity: 120 PC<br>Case Weight: 17.42 LB</div><div class="icons"><span class="icon"><svg><use href="#i-recycle"/></svg>RECYCLABLE</span><span class="icon"><svg><use href="#i-micro"/></svg>MICROWAVE SAFE</span></div></div></div>
    </div>
  </div>
</section>

<!-- Microwavable -->
<section class="spread" style="top:1178px">
  <div class="page">
    <div class="band">Rectangular Microwavable Food Container</div>
    <div class="grid">
      <div class="card"><div class="card-title">24oz Rectangular Microwavable<br>Container with Lid</div><div class="shot"><div class="ph black" role="img" aria-label="Black rectangular container with clear lid"></div><span class="code"># M1</span></div><div class="meta"><div class="specs">Color: Black Base, Clear Lid<br>Material: PP<br>Quantity: 150 Sets<br>Case Weight: 12.13 LB</div><div class="icons"><span class="icon"><svg><use href="#i-recycle"/></svg>RECYCLABLE</span><span class="icon"><svg><use href="#i-leak"/></svg>LEAK PROOF</span><span class="icon"><svg><use href="#i-micro"/></svg>MICROWAVE SAFE</span></div></div></div>
      <div class="card"><div class="card-title">28oz Rectangular Microwavable<br>Container with Lid</div><div class="shot"><div class="ph black" role="img" aria-label="Black rectangular container with clear lid"></div><span class="code"># M2</span></div><div class="meta"><div class="specs">Color: Black Base, Clear Lid<br>Material: PP<br>Quantity: 150 Sets<br>Case Weight: 14.55 LB</div><div class="icons"><span class="icon"><svg><use href="#i-recycle"/></svg>RECYCLABLE</span><span class="icon"><svg><use href="#i-leak"/></svg>LEAK PROOF</span><span class="icon"><svg><use href="#i-micro"/></svg>MICROWAVE SAFE</span></div></div></div>
      <div class="card"><div class="card-title">28oz Rectangular Microwavable<br>Container with Lid 2-compartment</div><div class="shot"><div class="ph black" role="img" aria-label="Black two-compartment container"></div><span class="code"># M3</span></div><div class="meta"><div class="specs">Color: Black Base, Clear Lid<br>Material: PP<br>Quantity: 150 Sets<br>Case Weight: 16.64 LB</div><div class="icons"><span class="icon"><svg><use href="#i-recycle"/></svg>RECYCLABLE</span><span class="icon"><svg><use href="#i-leak"/></svg>LEAK PROOF</span><span class="icon"><svg><use href="#i-micro"/></svg>MICROWAVE SAFE</span></div></div></div>
      <div class="card"><div class="card-title">39oz Rectangular Microwavable<br>Container with Lid 3-compartment</div><div class="shot"><div class="ph black" role="img" aria-label="Black three-compartment container"></div><span class="code"># M4</span></div><div class="meta"><div class="specs">Color: Black Base, Clear Lid<br>Material: PP<br>Quantity: 150 Sets<br>Case Weight: 22.7 LB</div><div class="icons"><span class="icon"><svg><use href="#i-recycle"/></svg>RECYCLABLE</span><span class="icon"><svg><use href="#i-leak"/></svg>LEAK PROOF</span><span class="icon"><svg><use href="#i-micro"/></svg>MICROWAVE SAFE</span></div></div></div>
    </div>
  </div>
  <div class="page right">
    <div class="band">Round Microwavable Food Container</div>
    <div class="grid">
      <div class="card"><div class="card-title">24oz Round Microwavable Container<br>with Lid</div><div class="shot"><div class="ph black round" role="img" aria-label="Black round container with clear lid"></div><span class="code"># M5</span></div><div class="meta"><div class="specs">Color: Black Base, Clear Lid<br>Material: PP<br>Quantity: 150 Sets<br>Case Weight: 12.68 LB</div><div class="icons"><span class="icon"><svg><use href="#i-recycle"/></svg>RECYCLABLE</span><span class="icon"><svg><use href="#i-leak"/></svg>LEAK PROOF</span><span class="icon"><svg><use href="#i-micro"/></svg>MICROWAVE SAFE</span></div></div></div>
      <div class="card"><div class="card-title">48oz Round Microwaveable Container<br>with Lid</div><div class="shot"><div class="ph black round" role="img" aria-label="Black round container with clear lid"></div><span class="code"># M6</span></div><div class="meta"><div class="specs">Color: Black Base, Clear Lid<br>Material: PP<br>Quantity: 150 Sets<br>Case Weight: 21.45 LB</div><div class="icons"><span class="icon"><svg><use href="#i-recycle"/></svg>RECYCLABLE</span><span class="icon"><svg><use href="#i-leak"/></svg>LEAK PROOF</span><span class="icon"><svg><use href="#i-micro"/></svg>MICROWAVE SAFE</span></div></div></div>
      <div class="card"><div class="card-title">36oz Microwaveable Noodle Bowl<br>with Lid</div><div class="shot"><div class="ph black round" role="img" aria-label="Black noodle bowl with clear lid"></div><span class="code"># M7</span></div><div class="meta"><div class="specs">Color: Black Base, Clear Lid<br>Material: PP<br>Quantity: 120 Sets<br>Case Weight: 12.13 LB</div><div class="icons"><span class="icon"><svg><use href="#i-recycle"/></svg>RECYCLABLE</span><span class="icon"><svg><use href="#i-leak"/></svg>LEAK PROOF</span><span class="icon"><svg><use href="#i-micro"/></svg>MICROWAVE SAFE</span></div></div></div>
      <div class="card"><div class="card-title">50oz Microwaveable Noodle Bowl with<br>Insert and Lid</div><div class="shot"><div class="ph black round" role="img" aria-label="Black noodle bowl with insert and lid"></div><span class="code"># M8</span></div><div class="meta"><div class="specs">Color: Black Base, Clear Lid<br>Material: PP<br>Quantity: 90 Sets<br>Case Weight: 15.56 LB</div><div class="icons"><span class="icon"><svg><use href="#i-recycle"/></svg>RECYCLABLE</span><span class="icon"><svg><use href="#i-leak"/></svg>LEAK PROOF</span><span class="icon"><svg><use href="#i-micro"/></svg>MICROWAVE SAFE</span></div></div></div>
    </div>
  </div>
</section>

<!-- Deli / Fold -->
<section class="spread" style="top:1736px">
  <div class="page">
    <div class="band">Deli Container</div>
    <div class="grid">
      <div class="card"><div class="card-title">12oz PP Deli Container with Lid</div><div class="shot"><div class="ph black tall" role="img" aria-label="Black deli cup with clear lid"></div><span class="code"># D1</span></div><div class="meta"><div class="specs">Color: Black Base, Clear Lid<br>Material: PP<br>Quantity: 240 Sets<br>Case Weight: 13.91 LB</div><div class="icons"><span class="icon"><svg><use href="#i-recycle"/></svg>RECYCLABLE</span><span class="icon"><svg><use href="#i-leak"/></svg>LEAK PROOF</span><span class="icon"><svg><use href="#i-micro"/></svg>MICROWAVE SAFE</span></div></div></div>
      <div class="card"><div class="card-title">16oz PP Deli Container with Lid</div><div class="shot"><div class="ph black tall" role="img" aria-label="Black deli cup with clear lid"></div><span class="code"># D2</span></div><div class="meta"><div class="specs">Color: Black Base, Clear Lid<br>Material: PP<br>Quantity: 240 Sets<br>Case Weight: 14.33 LB</div><div class="icons"><span class="icon"><svg><use href="#i-recycle"/></svg>RECYCLABLE</span><span class="icon"><svg><use href="#i-leak"/></svg>LEAK PROOF</span><span class="icon"><svg><use href="#i-micro"/></svg>MICROWAVE SAFE</span></div></div></div>
      <div class="card"><div class="card-title">24oz PP Deli Container with Lid</div><div class="shot"><div class="ph black tall" role="img" aria-label="Black deli cup with clear lid"></div><span class="code"># D3</span></div><div class="meta"><div class="specs">Color: Black Base, Clear Lid<br>Material: PP<br>Quantity: 240 Sets<br>Case Weight: 17.5 LB</div><div class="icons"><span class="icon"><svg><use href="#i-recycle"/></svg>RECYCLABLE</span><span class="icon"><svg><use href="#i-leak"/></svg>LEAK PROOF</span><span class="icon"><svg><use href="#i-micro"/></svg>MICROWAVE SAFE</span></div></div></div>
      <div class="card"><div class="card-title">32oz PP Deli Container with Lid</div><div class="shot"><div class="ph black tall" role="img" aria-label="Black deli cup with clear lid"></div><span class="code"># D4</span></div><div class="meta"><div class="specs">Color: Black Base, Clear Lid<br>Material: PP<br>Quantity: 240 Sets<br>Case Weight: 22.27 LB</div><div class="icons"><span class="icon"><svg><use href="#i-recycle"/></svg>RECYCLABLE</span><span class="icon"><svg><use href="#i-leak"/></svg>LEAK PROOF</span><span class="icon"><svg><use href="#i-micro"/></svg>MICROWAVE SAFE</span></div></div></div>
    </div>
  </div>
  <div class="page right">
    <div class="band">Fold-To-Go Box</div>
    <div class="grid">
      <div class="card"><div class="card-title">KRAFT TAKE-OUT BOX 5"*4.5"*2.5"</div><div class="shot"><div class="ph kraft" role="img" aria-label="Kraft paper fold-top take-out box"></div><span class="code">#F1</span></div><div class="meta"><div class="specs">Color: Kraft<br>Material: PP<br>Quantity: 450 PC</div><div class="icons"><span class="icon"><svg><use href="#i-recycle"/></svg>RECYCLABLE</span><span class="icon"><svg><use href="#i-micro"/></svg>MICROWAVE SAFE</span></div></div></div>
      <div class="card"><div class="card-title">KRAFT TAKE-OUT BOX 8.5"*6.25"*1.875"</div><div class="shot"><div class="ph kraft" role="img" aria-label="Kraft paper fold-top take-out box"></div><span class="code"># F2</span></div><div class="meta"><div class="specs">Color: Kraft<br>Material: PP<br>Quantity: 200 PC</div><div class="icons"><span class="icon"><svg><use href="#i-recycle"/></svg>RECYCLABLE</span><span class="icon"><svg><use href="#i-micro"/></svg>MICROWAVE SAFE</span></div></div></div>
      <div class="card"><div class="card-title">BLACK PAPER TAKE-OUT BOX<br>8.5"*6.25"*2.5"</div><div class="shot"><div class="ph boxblack" role="img" aria-label="Black paper fold-top take-out box"></div><span class="code"># F3</span></div><div class="meta"><div class="specs">Color: Black<br>Material: PP<br>Quantity: 200 PC</div><div class="icons"><span class="icon"><svg><use href="#i-recycle"/></svg>RECYCLABLE</span><span class="icon"><svg><use href="#i-micro"/></svg>MICROWAVE SAFE</span></div></div></div>
      <div class="card"><div class="card-title">BLACK PAPER TAKE-OUT BOX<br>8.5"*6.25"*3.5"</div><div class="shot"><div class="ph boxblack" role="img" aria-label="Black paper fold-top take-out box"></div><span class="code"># F4</span></div><div class="meta"><div class="specs">Color: Black<br>Material: PP<br>Quantity: 160 PC</div><div class="icons"><span class="icon"><svg><use href="#i-recycle"/></svg>RECYCLABLE</span><span class="icon"><svg><use href="#i-micro"/></svg>MICROWAVE SAFE</span></div></div></div>
    </div>
  </div>
</section>

<!-- Portion / Cold cup -->
<section class="spread" style="top:2294px">
  <div class="page">
    <div class="band">Portion Cup</div>
    <div class="grid">
      <div class="card"><div class="card-title">0.75oz Clear Portion Cup /<br>0.75/1oz Clear Portion Cup Lid</div><div class="shot"><div class="ph clear cup" role="img" aria-label="Clear portion cups with lids"></div><span class="code"># S1</span></div><div class="meta"><div class="specs">Color: Clear / Clear<br>Material: PP / PET<br>Quantity: 2500 PC / 2500 PC</div><div class="icons"><span class="icon"><svg><use href="#i-recycle"/></svg>RECYCLABLE</span><span class="icon"><svg><use href="#i-leak"/></svg>LEAK PROOF</span></div></div></div>
      <div class="card"><div class="card-title">1.5oz Clear Portion Cup /<br>1.5/2/2.5oz Clear Portion Cup Lid</div><div class="shot"><div class="ph clear cup" role="img" aria-label="Clear portion cups with lids"></div><span class="code"># S2</span></div><div class="meta"><div class="specs">Color: Clear / Clear<br>Material: PP / PET<br>Quantity: 2500 PC / 2500 PC</div><div class="icons"><span class="icon"><svg><use href="#i-recycle"/></svg>RECYCLABLE</span><span class="icon"><svg><use href="#i-leak"/></svg>LEAK PROOF</span></div></div></div>
      <div class="card"><div class="card-title">3.25oz Clear Portion Cup /<br>3.25/4/5.5oz Clear Portion Cup Lid</div><div class="shot"><div class="ph clear cup" role="img" aria-label="Clear portion cups with lids"></div><span class="code"># S3</span></div><div class="meta"><div class="specs">Color: Clear / Clear<br>Material: PP / PET<br>Quantity: 2500 PC / 2500 PC</div><div class="icons"><span class="icon"><svg><use href="#i-recycle"/></svg>RECYCLABLE</span><span class="icon"><svg><use href="#i-leak"/></svg>LEAK PROOF</span></div></div></div>
      <div class="card"><div class="card-title">1oz Clear Sause Container With Lid</div><div class="shot"><div class="ph clear cup" role="img" aria-label="Clear sauce containers with lids"></div><span class="code"># S4</span></div><div class="meta"><div class="specs">Color: Clear<br>Material: PP<br>Quantity: 2000 PC</div><div class="icons"><span class="icon"><svg><use href="#i-recycle"/></svg>RECYCLABLE</span><span class="icon"><svg><use href="#i-micro"/></svg>MICROWAVE SAFE</span></div></div></div>
    </div>
  </div>
  <div class="page right">
    <div class="band">Cold Drink Cup</div>
    <div class="grid">
      <div class="card"><div class="card-title">16oz Clear PET Cup /<br>Flat Lids For 12-24oz PET Cup</div><div class="shot"><div class="ph clear glass" role="img" aria-label="Clear plastic drink cup"></div><span class="code"># P1</span></div><div class="meta"><div class="specs">Color: Clear / Clear<br>Material: PET / PET<br>Quantity: 1000 PC / 1000 PC</div><div class="icons"><span class="icon"><svg><use href="#i-recycle"/></svg>RECYCLABLE</span><span class="icon"><svg><use href="#i-leak"/></svg>LEAK PROOF</span></div></div></div>
      <div class="card"><div class="card-title">KRAFT TAKE-OUT BOX 8.5"*6.25"*1.875"</div><div class="shot"><div class="ph clear glass" role="img" aria-label="Clear plastic drink cup"></div><span class="code"># P2</span></div><div class="meta"><div class="specs">Color: Clear / Clear<br>Material: PET / PET<br>Quantity: 1000 PC / 1000 PC</div><div class="icons"><span class="icon"><svg><use href="#i-recycle"/></svg>RECYCLABLE</span><span class="icon"><svg><use href="#i-leak"/></svg>LEAK PROOF</span></div></div></div>
      <div class="card"><div class="card-title">16oz Frosted PP Injection Cup /<br>Black Lid With Heart Stopper For PP Cups</div><div class="shot"><div class="ph clear glass" role="img" aria-label="Frosted plastic drink cup"></div><span class="code"># P3</span></div><div class="meta"><div class="specs">Color: White / Black<br>Material: PP / PP<br>Quantity: 500 PC / 500 PC</div><div class="icons"><span class="icon"><svg><use href="#i-recycle"/></svg>RECYCLABLE</span><span class="icon"><svg><use href="#i-leak"/></svg>LEAK PROOF</span></div></div></div>
      <div class="card"><div class="card-title">24oz Frosted PP Injection Cup /<br>White Lid With Heart Stopper For PP Cups</div><div class="shot"><div class="ph clear glass" role="img" aria-label="Frosted plastic drink cup"></div><span class="code"># P4</span></div><div class="meta"><div class="specs">Color: White / White<br>Material: PP / PP<br>Quantity: 500 PC / 500 PC</div><div class="icons"><span class="icon"><svg><use href="#i-recycle"/></svg>RECYCLABLE</span><span class="icon"><svg><use href="#i-leak"/></svg>LEAK PROOF</span></div></div></div>
    </div>
  </div>
</section>

<!-- Utensils / Misc -->
<section class="spread" style="top:2852px">
  <div class="page">
    <div class="band">Utensils</div>
    <div class="grid">
      <div class="card"><div class="card-title">21cm Bamboo Chopsticks<br>Paper Warpped　(Twin)</div><div class="shot"><div class="ph wood long" role="img" aria-label="Paper-wrapped bamboo chopsticks"></div><span class="code"># U1</span></div><div class="meta"><div class="specs">Color: White<br>Material: bamboo<br>Quantity: 2000 PRS</div><div class="icons"><span class="icon"><svg><use href="#i-recycle"/></svg>RECYCLABLE</span></div></div></div>
      <div class="card"><div class="card-title">Heavy Weight Warpped<br>Cutlery Kit 6 In 1</div><div class="shot"><div class="ph clear" role="img" aria-label="Wrapped white cutlery kit"></div><span class="code"># U2</span></div><div class="meta"><div class="specs">Color: White<br>Material: PP<br>Quantity: 250 Sets</div><div class="icons"><span class="icon"><svg><use href="#i-recycle"/></svg>RECYCLABLE</span></div></div></div>
      <div class="card"><div class="card-title">Heavy Duty Weight Soup Spoon</div><div class="shot"><div class="ph black long" role="img" aria-label="Black plastic soup spoon"></div><span class="code"># U3</span></div><div class="meta"><div class="specs">Color: Black<br>Material: PP<br>Quantity: 1000 PC</div><div class="icons"><span class="icon"><svg><use href="#i-recycle"/></svg>RECYCLABLE</span></div></div></div>
      <div class="card"><div class="card-title">Heavy Duty Weight Fork</div><div class="shot"><div class="ph black long" role="img" aria-label="Black plastic fork"></div><span class="code"># U4</span></div><div class="meta"><div class="specs">Color: Black<br>Material: PP<br>Quantity: 1000 PC</div><div class="icons"><span class="icon"><svg><use href="#i-recycle"/></svg>RECYCLABLE</span></div></div></div>
    </div>
  </div>
  <div class="page right">
    <div class="band">Miscellaneous</div>
    <div class="grid">
      <div class="card"><div class="card-title">Dinner Napkin 2-PLY 17"×14"</div><div class="shot"><div class="ph clear" role="img" aria-label="Folded white dinner napkin"></div><span class="code"># M1</span></div><div class="meta"><div class="specs">Color: White<br>Material: bamboo<br>Quantity: 2000 PRS</div><div class="icons"><span class="icon"><svg><use href="#i-recycle"/></svg>RECYCLABLE</span></div></div></div>
      <div class="card"><div class="card-title">Interfold Napkin 2-PLY 7.9"×6.5"</div><div class="shot"><div class="ph white tall" role="img" aria-label="Stack of interfold napkins"></div><span class="code"># M2</span></div><div class="meta"><div class="specs">Color: White<br>Material: PP<br>Quantity: 250 Sets</div><div class="icons"><span class="icon"><svg><use href="#i-recycle"/></svg>RECYCLABLE</span></div></div></div>
      <div class="card"><div class="card-title">Heavy Duty Full Size Deep Aluminum Pan</div><div class="shot"><div class="ph silver" role="img" aria-label="Full size aluminum pan"></div><span class="code"># M3</span></div><div class="meta"><div class="specs">Color: Black<br>Material: PP<br>Quantity: 1000 PC</div><div class="icons"><span class="icon"><svg><use href="#i-recycle"/></svg>RECYCLABLE</span></div></div></div>
      <div class="card"><div class="card-title">Heavy Duty 18"X500' Aluminum<br>Foil Roll 19mic</div><div class="shot"><div class="ph silver" role="img" aria-label="Boxed aluminum foil roll"></div><span class="code"># M4</span></div><div class="meta"><div class="specs">Color: Black<br>Material: PP<br>Quantity: 1000 PC</div><div class="icons"><span class="icon"><svg><use href="#i-recycle"/></svg>RECYCLABLE</span></div></div></div>
    </div>
  </div>
</section>

<!-- Bags -->
<section class="spread" style="top:3410px">
  <div class="page">
    <div class="band">Miscellaneous</div>
    <div class="stack">
      <div class="card wide"><div class="card-title"><span class="num"># M5</span>T-Shirt Carry Out Bags</div>
        <div class="variants">
          <div class="variant"><div class="art bag" role="img" aria-label="White t-shirt bag, small"></div>#1 8"×6"×16" 12.5MIC</div>
          <div class="variant"><div class="art bag" role="img" aria-label="White t-shirt bag, medium"></div>#3 10.5"×6"×20" 15MIC</div>
          <div class="variant"><div class="art bag" role="img" aria-label="White t-shirt bag, large"></div>#5 12"×7"×22" 17MIC</div>
        </div>
        <div class="meta"><div class="specs">Color: White<br>Quantity: 1000 BAGS</div><div class="icons"><span class="icon"><svg><use href="#i-recycle"/></svg>RECYCLABLE</span></div></div></div>
      <div class="card wide"><div class="card-title"><span class="num"># M6</span>Trash Bags</div>
        <div class="variants">
          <div class="variant"><div class="art trash" role="img" aria-label="Tied trash bag"></div>#33 GALLONS 1.2MIL</div>
          <div class="variant"><div class="art trash" role="img" aria-label="Tied trash bag"></div>#55-60 GALLONS 1.4MIL</div>
        </div>
        <div class="meta"><div class="specs">Color: Black<br>Quantity: 100 BAGS</div><div class="icons"><span class="icon"><svg><use href="#i-recycle"/></svg>RECYCLABLE</span></div></div></div>
    </div>
  </div>
  <div class="page right">
    <div class="band">Miscellaneous</div>
    <div class="stack">
      <div class="card wide"><div class="card-title"><span class="num"># M7</span>Kaft Paper Bag With Twist Handle</div>
        <div class="variants">
          <div class="variant"><div class="art paperbag" role="img" aria-label="Paper bag with twist handle, small"></div>#3 8"*4.5"*10.25"</div>
          <div class="variant"><div class="art paperbag" role="img" aria-label="Paper bag with twist handle, medium"></div>#5 10"*6.75"*12"</div>
          <div class="variant"><div class="art paperbag" role="img" aria-label="Paper bag with twist handle, large"></div>#10 13"*7"*13"</div>
        </div>
        <div class="meta"><div class="specs">Color: Kraft<br>Quantity: 1000 BAGS</div><div class="icons"><span class="icon"><svg><use href="#i-recycle"/></svg>RECYCLABLE</span></div></div></div>
      <div class="pair">
        <div class="card"><div class="card-title">Thermal Paper 3-1/8"*230'</div><div class="shot"><div class="ph clear cup" role="img" aria-label="Roll of thermal receipt paper"></div><span class="code">M8</span></div><div class="meta"><div class="specs">Quantity: 50 Roll</div><div class="icons"><span class="icon"><svg><use href="#i-recycle"/></svg>RECYCLABLE</span></div></div></div>
        <div class="card empty"></div>
      </div>
    </div>
  </div>
</section>

<!-- Custom printing / News -->
<section class="spread" style="top:3968px">
  <div class="page">
    <div class="band">Custom Printing</div>
    <div class="lead">Ready to take your brand to the next level?</div>
    <div class="promo">
      <p>Our custom printing services for disposable food boxes are here to make your packaging pop!</p>
      <p>Why choose us?</p>
      <p><b>Vibrant Colors:</b>Stand out with eye-catching designs that grab attention.</p>
      <p><b>High-Quality Printing:</b>Get crisp, clear images that showcase your brand beautifully.</p>
      <p><b>Branding and Logos:</b>Make your mark with custom logos and branding that customers won't forget.</p>
      <p>From food trucks to catering businesses, our custom printed food boxes are a game-changer! Let your packaging do the talking and leave a lasting impression on your customers.</p>
      <p class="cta">Get in touch today and let's elevate your brand!</p>
    </div>
    <div class="collage" role="img" aria-label="Collage of custom printed paper food boxes and bags"></div>
  </div>
  <div class="page right">
    <div class="band">News</div>
    <div class="news">
      <div class="headline">Headline</div>
      <div class="col a">Lorem ipsum dolor sit amet, consectetur adipiscing elit, sed do eiusmod tempor incididunt ut labore et dolore magna aliqua. Ut enim ad minim veniam, quis nostrud exercitation ullamco laboris nisi ut aliquip ex ea commodo consequat. Duis aute irure dolor in reprehenderit. Sed ut perspiciatis unde omnis iste natus error sit voluptatem accusantium doloremque laudantium, totam rem aperiam, eaque ipsa quae ab illo inventore veritatis et quasi architecto beatae vitae dicta sunt explicabo. Nemo enim ipsam voluptatem quia voluptas sit aspernatur aut odit aut fugit, sed quia consequuntur magni dolores eos qui ratione voluptatem sequi nesciunt. Neque porro quisquam est, qui dolorem ipsum quia dolor sit amet, consectetur, adipisci velit, sed quia non numquam eius modi. Sed ut perspiciatis unde omnis iste natus error sit voluptatem accusantium doloremque laudantium, totam rem aperiam, eaque ipsa quae ab illo inventore veritatis et quasi architecto beatae vitae dicta sunt explicabo. Nemo enim ipsam voluptatem quia voluptas sit aspernatur aut odit aut fugit, sed quia consequuntur magni dolores eos qui ratione voluptatem sequi nesciunt. Neque porro quisquam est, qui dolorem ipsum quia dolor sit amet, consectetur, adipisci velit, sed quia non.</div>
      <div class="col b">Lorem ipsum dolor sit amet, consectetur adipiscing elit, sed do eiusmod tempor incididunt ut labore et dolore magna aliqua. Ut enim ad minim veniam, quis nostrud exercitation ullamco laboris nisi ut aliquip ex ea commodo consequat. Duis aute irure dolor in.</div>
      <div class="news-photo" role="img" aria-label="Black microwavable containers with clear lids, one filled with a meal"></div>
    </div>
  </div>
</section>

</body>
</html>
```